Refresh old packing for HGH product

At now product has design like on photo.
Target is to make new one based on this. New one should be more medical, and luxury looks.

Colors
0054AA
0677BA
7BADD7
CADEEF
E8F1F8

```html
<!DOCTYPE html>
<html lang="en">
<head>
<meta charset="utf-8">
<title>Somatropin Box Front – Kelva Laboratories</title>
<link rel="stylesheet" href="https://fonts.googleapis.com/css2?family=Montserrat:wght@500;600;700;800;900&display=swap">
<style>
  :root {
    --navy: #0054AA;
    --blue: #0677BA;
    --tab-blue: #2FA3DC;
    --sky: #7BADD7;
    --pale: #CADEEF;
    --mist: #E8F1F8;
    --ink: #0E2A4A;
    --card: #FFFFFF;
    --stage: #6B767C;
  }
  * { box-sizing: border-box; margin: 0; padding: 0; }
  html, body {
    width: 1200px; height: 840px; overflow: hidden;
    background: var(--stage);
    font-family: "Montserrat", sans-serif;
  }
  .canvas { position: relative; width: 1200px; height: 840px; }
  .box-front {
    position: absolute; left: 100px; top: 110px;
    width: 1000px; height: 620px;
    background: linear-gradient(180deg, var(--card) 0%, #F7F9FB 100%);
    overflow: hidden;
    box-shadow: 0 24px 50px rgba(0,0,0,0.28);
  }
  .brand-tab { position: absolute; left: 0; top: 0; width: 460px; height: 130px; }
  .brand {
    position: absolute; left: 34px; top: 30px;
    display: flex; align-items: center; gap: 14px;
    color: #fff; font-weight: 700; font-size: 22px; line-height: 1.05;
    letter-spacing: 0.5px;
  }
  .brand-dot { width: 54px; height: 54px; border-radius: 50%; border: 3px solid #fff; }
  .dna-art {
    position: absolute; left: 430px; top: 0; width: 570px; height: 360px;
    background: radial-gradient(ellipse at 65% 40%, rgba(123,173,215,0.45) 0%, rgba(202,222,239,0.35) 40%, rgba(232,241,248,0) 75%);
  }
  .pack-size {
    position: absolute; right: 28px; top: 18px;
    font-size: 11px; font-weight: 600; color: var(--ink); letter-spacing: 0.3px;
  }
  .emblem-art {
    position: absolute; left: 120px; top: 285px; width: 110px; height: 140px;
    background: radial-gradient(ellipse at 50% 40%, var(--sky) 0%, var(--pale) 55%, rgba(232,241,248,0) 80%);
    border-radius: 12px;
  }
  .product { position: absolute; left: 250px; top: 295px; white-space: nowrap; }
  .product-name {
    font-size: 80px; font-weight: 900; color: var(--blue);
    letter-spacing: 1px; line-height: 1;
  }
  .product-desc {
    margin-top: 10px; margin-left: 4px;
    font-size: 19px; font-weight: 700; color: var(--navy); letter-spacing: 0.6px;
  }
  .storage {
    position: absolute; right: 40px; top: 440px; text-align: right;
    font-size: 14px; font-weight: 700; color: var(--ink); line-height: 1.4;
    white-space: nowrap;
  }
  .diluent {
    position: absolute; left: 90px; bottom: 60px;
    font-size: 20px; font-weight: 700; color: var(--ink); letter-spacing: 0.6px;
  }
</style>
</head>
<body>
<main class="canvas">
  <section class="box-front">
    <svg class="brand-tab" viewBox="0 0 460 130" aria-hidden="true">
      <path d="M0 0 H440 C400 0 380 40 360 80 C345 110 320 118 290 118 H0 Z" fill="var(--tab-blue)"/>
    </svg>
    <div class="brand">
      <span class="brand-dot"></span>
      <span>KELVA<br>LABORATORIES</span>
    </div>

    <div class="dna-art" role="img" aria-label="Faint DNA double helix and molecular structure pattern in light blue and grey"></div>
    <p class="pack-size">100IU BOX - 10 VIAL X 10IU (3.33MG)</p>

    <div class="emblem-art" role="img" aria-label="Winged medical staff emblem in blue"></div>
    <div class="product">
      <h1 class="product-name">SOMATROPIN</h1>
      <p class="product-desc">OMATROPIN (RDNA ORIGIN) FOR INJECTION</p>
    </div>

    <p class="storage">STORE BETWEEN 2-8<br>PROTECT FROM LIGHT.<br>DO NOT SHAKE</p>
    <p class="diluent">1 VIAL X 10ML STERILE DILUTENT</p>
  </section>
</main>
</body>
</html>
```